Dental specialist needs a sharp looking letterhead

I am looking for a letterhead to be used to send letters and communication between myself (a dental specialist) and other dentists.
My office is a state of the art dental specialty office.
I need to letterhead to also state:
Derek L. Halvorsen DDS
2847 Birchmont Avenue, Suite K
West Larkdale, NY 14390
(716)555-0193
fax: (716)555-0157
halvorsenpulp.com (**this email address may change)

i included my logo designs.
thank you

Target Market(s)

dentists

Industry/Entity Type

Communication

Requirements
Must have
• the included logo, whether the vertical or horizontal versions

```html
<!DOCTYPE html>
<html lang="en">
<head>
<meta charset="utf-8">
<title>Keystone Endodontics P.C. – Letterhead</title>
<link rel="stylesheet" href="https://fonts.googleapis.com/css2?family=Open+Sans:wght@400;600&display=swap">
<style>
  :root {
    --backdrop: #1b1b1b;
    --paper: #ffffff;
    --ink: #3a3a3a;
    --ink-dark: #1f1f1f;
    --brand-blue: #2aaee8;
    --brand-blue-light: #5cc6f2;
    --brand-green: #8cc63f;
  }
  * { box-sizing: border-box; margin: 0; padding: 0; }
  html, body {
    width: 1200px;
    height: 750px;
    overflow: hidden;
    background: var(--backdrop);
    font-family: "Open Sans", Arial, sans-serif;
  }
  .letterhead {
    position: absolute;
    left: 325px;
    top: 19px;
    width: 550px;
    height: 712px;
    background: var(--paper);
    box-shadow: 0 6px 24px rgba(0, 0, 0, 0.5);
  }
  .masthead {
    position: absolute;
    left: 36px;
    top: 44px;
  }
  .brand {
    display: flex;
    align-items: center;
    gap: 7px;
  }
  .brand-dot {
    width: 14px;
    height: 14px;
    border-radius: 50%;
    background: var(--brand-blue);
  }
  .brand-name {
    font-size: 11px;
    font-weight: 600;
    color: var(--ink-dark);
    letter-spacing: 0.2px;
  }
  .doctor {
    margin: 6px 0 0 21px;
    font-size: 10px;
    color: var(--brand-blue);
    letter-spacing: 1.5px;
  }
  .doctor-title {
    display: block;
    margin-top: 1px;
    padding-left: 78px;
    font-size: 8px;
    color: var(--brand-green);
    letter-spacing: 1px;
  }
  .letter-body {
    position: absolute;
    left: 200px;
    top: 118px;
    width: 310px;
    font-size: 7.2px;
    line-height: 1.5;
    color: var(--ink);
  }
  .letter-body p { margin-bottom: 9px; }
  .letter-body .salutation { margin-bottom: 11px; }
  .sign-off {
    position: absolute;
    left: 200px;
    top: 520px;
    font-size: 7.2px;
    color: var(--ink);
  }
  .footer-band {
    position: absolute;
    left: 0;
    right: 0;
    top: 612px;
    height: 30px;
    background: linear-gradient(to bottom, var(--brand-blue-light), var(--brand-blue));
    display: flex;
    align-items: center;
    justify-content: center;
    font-size: 8.6px;
    color: var(--paper);
    letter-spacing: 0.2px;
  }
  .footer-band .divider { margin: 0 7px; opacity: 0.85; }
  .website {
    position: absolute;
    left: 0;
    right: 0;
    top: 654px;
    text-align: center;
    font-size: 9px;
    letter-spacing: 4.5px;
    color: var(--ink-dark);
  }
</style>
</head>
<body>
  <main class="letterhead">
    <header class="masthead">
      <div class="brand">
        <span class="brand-dot"></span>
        <span class="brand-name">Keystone Endodontics P.C.</span>
      </div>
      <p class="doctor">Derek L. Halvorsen <span class="doctor-title">DDS</span></p>
    </header>

    <section class="letter-body">
      <p class="salutation">Dear Colleague,</p>
      <p>Thank you for referring your patient to our office. We completed the initial examination and radiographs today, and the findings are summarized below for your records.</p>
      <p>The tooth showed signs of irreversible pulpitis, and root canal therapy was started under local anesthesia without complications.</p>
      <p>Treatment will be completed at the next visit. Please schedule a final restoration within four weeks to protect the tooth.</p>
      <p>A copy of the radiographs and our clinical notes is enclosed. We will send a follow-up report once treatment is finished.</p>
      <p>Should you have any questions, please feel free to contact our office at any time.</p>
    </section>

    <p class="sign-off">Sincerely,</p>

    <footer>
      <div class="footer-band">
        <span>Address: 2847 Birchmont Avenue, Suite K West Larkdale, NY 14390</span>
        <span class="divider">|</span>
        <span>Phone: (716)555-0193</span>
        <span class="divider">|</span>
        <span>Fax: (716)555-0157</span>
      </div>
      <p class="website">www.halvorsenpulp.com</p>
    </footer>
  </main>
</body>
</html>
```